Business card for home decor store and design

I need a business card for my home decor boutique that’s professional looking boho/rustic. We sell vintage furniture, vintage finds, lamps, throws, rugs. We also carry a Diy paint line for refinishing furniture. We offer workshop on painting furniture, private or group setting. We in the heart of Old Town Red Bluff. We love to design, build and restore. Family owned small business. Our style is rustic boho farmhouse. We search for one of a kind found and repurposed items. We love vintage home decor, vintage windows.

Target Market(s)

Home decor

Industry/Entity Type

Home Accessories

Contact Information for Business Card

Have a rustic look/boho

Font styles to use
Serif
Script

Requirements
Must have
• Logo

```html
<!DOCTYPE html>
<html lang="en">
<head>
<meta charset="utf-8">
<title>Birch &amp; Loam Co. — Business Card</title>
<link href="https://fonts.googleapis.com/css2?family=Montserrat:wght@400;500&family=Great+Vibes&display=swap" rel="stylesheet">
<style>
  :root {
    --stage: #3a3a3a;
    --card: #141414;
    --gold: #c9985f;
    --emboss: #333333;
    --emboss-line: #3a3a3a;
  }
  html, body {
    margin: 0;
    width: 799px;
    height: 1200px;
    overflow: hidden;
    background: var(--stage);
  }
  .canvas {
    position: relative;
    width: 799px;
    height: 1200px;
  }
  .card {
    position: absolute;
    left: 90px;
    width: 620px;
    height: 354px;
    background: var(--card);
    border-radius: 4px;
    overflow: hidden;
    box-shadow: 0 10px 30px rgba(0,0,0,.45);
  }
  .card--front { top: 130px; }
  .card--back  { top: 716px; }

  .brand-mark {
    position: absolute;
    display: flex;
    align-items: center;
    justify-content: center;
    border-radius: 50%;
    box-sizing: border-box;
  }
  .card--front .brand-mark {
    left: 210px; top: 77px;
    width: 200px; height: 200px;
    border: 6px solid var(--emboss-line);
  }
  .card--back .brand-mark {
    left: 380px; top: 130px;
    width: 190px; height: 190px;
    border: 6px solid var(--gold);
  }
  .brand-name {
    font-family: "Montserrat", sans-serif;
    font-weight: 500;
    white-space: nowrap;
    letter-spacing: .3px;
  }
  .card--front .brand-name { color: var(--emboss); font-size: 17px; }
  .card--back  .brand-name { color: var(--gold); font-size: 16px; }

  .edge-curve { position: absolute; left: 0; top: 0; }

  .person {
    position: absolute;
    left: 48px; top: 38px;
    color: var(--gold);
  }
  .person__name {
    font-family: "Great Vibes", cursive;
    font-size: 34px;
    line-height: 1;
  }
  .person__role {
    font-family: "Montserrat", sans-serif;
    font-size: 13px;
    margin-top: 4px;
  }
  .contact {
    position: absolute;
    left: 48px; top: 178px;
    font-family: "Montserrat", sans-serif;
    font-size: 13px;
    color: var(--gold);
    line-height: 19px;
  }
  .contact__address { margin: 0 0 6px 0; }
  .contact__row { display: flex; align-items: center; gap: 10px; }
  .contact__row svg { width: 13px; height: 13px; fill: var(--gold); }
</style>
</head>
<body>
<main class="canvas">

  <section class="card card--front" aria-label="Business card front">
    <div class="brand-mark">
      <span class="brand-name">Birch &amp; Loam Co.</span>
    </div>
  </section>

  <section class="card card--back" aria-label="Business card back">
    <svg class="edge-curve" width="40" height="120" viewBox="0 0 40 120">
      <path d="M0 0 H26 Q4 60 0 120 Z" fill="var(--gold)"/>
    </svg>

    <div class="person">
      <div class="person__name">Mara Ellison</div>
      <div class="person__role">Managing Director</div>
    </div>

    <div class="contact">
      <p class="contact__address">18 Willow Lane, Elm Falls,<br>Fernvale, US 450127</p>
      <div class="contact__row">
        <svg viewBox="0 0 16 16"><path d="M3 1h3l1 4-2 1a9 9 0 0 0 5 5l1-2 4 1v3a2 2 0 0 1-2 2A13 13 0 0 1 1 3a2 2 0 0 1 2-2z"/></svg>
        <span>555-014-2290</span>
      </div>
      <div class="contact__row">
        <svg viewBox="0 0 16 16"><path d="M1 3h14v10H1z M2 4l6 5 6-5" fill="none" stroke="var(--gold)" stroke-width="1.5"/></svg>
        <span>mara@birchloam.com</span>
      </div>
      <div class="contact__row">
        <svg viewBox="0 0 16 16"><circle cx="8" cy="8" r="6.5" fill="none" stroke="var(--gold)" stroke-width="1.5"/><path d="M1.5 8h13M8 1.5c-3 3-3 10 0 13M8 1.5c3 3 3 10 0 13" fill="none" stroke="var(--gold)" stroke-width="1.2"/></svg>
        <span>www.birchloam.com</span>
      </div>
    </div>

    <div class="brand-mark">
      <span class="brand-name">Birch &amp; Loam Co.</span>
    </div>
  </section>

</main>
</body>
</html>
```